"Sun On Water" Gospel Presentation Booklet

I need a design for a 12 page (including front/back cover) square booklet, with religious images and aesthetically pleasing fonts/designs. I want it to be very simple, and very straightforward. The main focus of the project is it's content. So the design should be very nice, but also should point to the content, not take away from it, or create distraction. People should be more focused on the words than the imagery.

I enjoy modern designs, I need a sharp aesthetic that is clean and neat. Nothing over the top.
I have attached a word document with the content I would like on the pages.

Colors
0592cd
0255a3
33a6d7
85cae6
85acd3
3276b5
9bcb3b
f04a50
f68d4c

Requirements
Should not have
• Super feminine colors/aesthetics

```html
<!DOCTYPE html>
<html lang="en">
<head>
<meta charset="utf-8">
<title>Sun On Water – Booklet Spread</title>
<link href="https://fonts.googleapis.com/css2?family=Anton&family=Bebas+Neue&display=swap" rel="stylesheet">
<style>
  :root {
    --olive: #93891a;
    --navy: #1d5596;
    --paper: #ffffff;
    --rule: #d4d4d4;
    --frame: #2a2a2a;
  }
  html, body {
    margin: 0;
    padding: 0;
    width: 1200px;
    height: 1200px;
    overflow: hidden;
    background: var(--paper);
  }
  .canvas {
    position: relative;
    width: 1200px;
    height: 1200px;
    box-sizing: border-box;
    border: 1px solid var(--frame);
    background: var(--paper);
  }
  .page {
    position: absolute;
    width: 575px;
    height: 575px;
    box-sizing: border-box;
    overflow: hidden;
  }
  .page--olive { left: 25px; top: 17px; background: var(--olive); }
  .page--title { left: 600px; top: 17px; border: 1px solid var(--rule); border-left: none; background: var(--paper); }
  .page--word  { left: 25px; top: 607px; border: 1px solid var(--rule); background: var(--paper); }
  .page--message { left: 600px; top: 607px; background: var(--navy); }

  .title-art, .word-art {
    position: absolute;
    left: 0;
    top: 0;
    width: 575px;
    height: 575px;
  }
  .display {
    font-family: 'Anton', sans-serif;
  }

  .message {
    position: absolute;
    left: 166px;
    top: 212px;
    margin: 0;
    font-family: 'Bebas Neue', sans-serif;
    font-size: 30px;
    line-height: 37px;
    color: var(--paper);
    letter-spacing: 0;
  }
  .message__line { display: block; white-space: nowrap; }
  .message__line--highlight {
    display: inline-block;
    color: var(--navy);
    background: var(--paper);
    padding-right: 5px;
    box-shadow: -166px 0 0 var(--paper);
  }
</style>
</head>
<body>
<main class="canvas">
  <section class="page page--olive" aria-label="Cover panel"></section>

  <section class="page page--title">
    <svg class="title-art" viewBox="0 0 575 575" xmlns="http://www.w3.org/2000/svg">
      <defs>
        <linearGradient id="landscapeFill" x1="0" y1="87" x2="0" y2="487" gradientUnits="userSpaceOnUse">
          <stop offset="0" stop-color="#5e6577"/>
          <stop offset="0.18" stop-color="#d9ceaa"/>
          <stop offset="0.34" stop-color="#8f98a6"/>
          <stop offset="0.5" stop-color="#7fa655"/>
          <stop offset="0.75" stop-color="#4f8a2c"/>
          <stop offset="1" stop-color="#2f5a1e"/>
        </linearGradient>
        <linearGradient id="doveFill" x1="0" y1="0" x2="0" y2="1">
          <stop offset="0" stop-color="#f2f2f0"/>
          <stop offset="1" stop-color="#dcdad6"/>
        </linearGradient>
      </defs>
      <g class="display" fill="url(#landscapeFill)" role="img" aria-label="Title lettering filled with a sunrise sky over green hills">
        <text x="80" y="211" font-size="144" textLength="344" lengthAdjust="spacingAndGlyphs">SUN</text>
        <text x="80" y="349" font-size="144" textLength="168" lengthAdjust="spacingAndGlyphs">ON</text>
        <text x="80" y="487" font-size="144" textLength="414" lengthAdjust="spacingAndGlyphs">WATER</text>
      </g>
      <ellipse cx="320" cy="288" rx="32" ry="50" fill="url(#doveFill)" role="img" aria-label="White dove in flight"/>
    </svg>
  </section>

  <section class="page page--word">
    <svg class="word-art" viewBox="0 0 575 575" xmlns="http://www.w3.org/2000/svg">
      <defs>
        <linearGradient id="cosmosFill" x1="179" y1="0" x2="397" y2="0" gradientUnits="userSpaceOnUse">
          <stop offset="0" stop-color="#3a3a7a"/>
          <stop offset="0.45" stop-color="#6f86c9"/>
          <stop offset="0.7" stop-color="#4a4f9a"/>
          <stop offset="1" stop-color="#2c3270"/>
        </linearGradient>
      </defs>
      <text class="display" x="179" y="327" font-size="91" textLength="218" lengthAdjust="spacingAndGlyphs" fill="url(#cosmosFill)" role="img" aria-label="Lettering filled with a starry galaxy">GOD</text>
    </svg>
  </section>

  <section class="page page--message">
    <p class="message">
      <span class="message__line">Sun On Water,</span>
      <span class="message__line message__line--highlight">That means he's perfect.</span>
      <span class="message__line">In fact, he is so perfect,</span>
      <span class="message__line">corruption cannot live</span>
      <span class="message__line">with him.</span>
    </p>
  </section>
</main>
</body>
</html>
```